Remodeling brochure

We need an informative homeowner friendly brochure detailing our company and things we do. We are looking for an initial setup and ideas (# of pages, etc) and then we will send more content. We are uploading our logo design. We are a high end remodeling company specializing in kitchen & bath remodels. We sell ourselves on customer communication and attention to detail in our designs and remodels.

Target Market(s)

Residential homeowners

Contact Information for Business Card

Modern and attention grabbing

Requirements
Must have
• Name- Hearth & Tile Crafters<br/>Address- 782 NW Larkspur Lane Suite #217<br/> Ankeny, Iowa 50894<br/>Phone- 515-482-7395<br/>email-htcraftersmidwest@pinemail.net

```html
<!DOCTYPE html>
<html lang="en">
<head>
<meta charset="utf-8">
<title>Hearth &amp; Tile Crafters — Remodeling Brochure</title>
<link href="https://fonts.googleapis.com/css2?family=Bebas+Neue&family=Fira+Sans:wght@400;500;600;700&family=Open+Sans:wght@400;600;800&family=Oswald:wght@500&display=swap" rel="stylesheet">
<style>
:root{
  --board:#a97c52;
  --ink:#2b2b2d;
  --ink-deep:#202022;
  --blue:#1a8fd6;
  --blue-deep:#1d5fb4;
  --paper:#f7f7f7;
  --paper-mid:#eeeff1;
  --grey:#b9babd;
  --white:#ffffff;
  --text:#4a4a4a;
}
*{box-sizing:border-box;margin:0;padding:0}
html,body{width:936px;height:1200px;overflow:hidden;background:var(--board)}
body{position:relative;font-family:"Open Sans",sans-serif;color:var(--text)}
.label{position:absolute;font-family:"Open Sans",sans-serif;font-weight:800;color:var(--white);font-size:22px;transform:translateX(-50%);white-space:nowrap}
.spread{position:absolute;left:137px;width:674px;box-shadow:2px 3px 6px rgba(0,0,0,.35);overflow:hidden}
.outer{top:115px;height:479px;background:var(--ink)}
.inner{top:616px;height:480px;background:var(--paper)}
.abs{position:absolute}
.photo{position:absolute;border-radius:4px}

/* outside */
.back-panel{left:0;top:0;width:337px;height:420px;background:radial-gradient(circle at 40% 55%,#5a5a5c 0%,#3a3a3c 45%,#252527 100%)}
.back-title{left:31px;top:28px;width:180px;font-family:"Fira Sans",sans-serif;font-weight:500;color:var(--white);font-size:12.5px;line-height:15.5px}
.back-copy{left:31px;top:84px;width:215px;font-size:5.9px;line-height:9.7px;color:#e6e6e6}
.section-head{font-family:"Fira Sans",sans-serif;font-weight:500;color:var(--blue)}
.contact-head{left:30px;top:325px;font-family:"Fira Sans",sans-serif;font-weight:600;color:var(--white);font-size:7.6px}
.contact-mail{left:30px;top:337px;font-size:5.9px;color:#e6e6e6;letter-spacing:.3px}
.tagline{left:377px;width:257px;top:325px;text-align:center;font-family:"Fira Sans",sans-serif;font-weight:500;color:var(--white);font-size:13.6px;line-height:16.5px}
.footer-band{left:0;top:420px;width:674px;height:28px;background:var(--white)}
.footer-dark{left:0;top:448px;width:674px;height:31px;background:var(--ink-deep)}
.fold{position:absolute;left:337px;top:0;width:1px;height:100%;background:rgba(0,0,0,.12)}
.brand-name{font-family:"Fira Sans",sans-serif;font-weight:500;color:var(--blue-deep);white-space:nowrap}
.brand-mark{display:inline-block;background:var(--blue-deep);vertical-align:middle}
.foot-phone{left:209px;top:425px;font-family:"Fira Sans",sans-serif;font-weight:700;font-size:16px;color:var(--blue-deep)}
.foot-services{left:345px;width:325px;top:422px;text-align:center;font-family:"Fira Sans",sans-serif;font-size:8px;line-height:11.5px;color:var(--blue-deep)}
.foot-address{left:26px;top:452px;font-size:5.3px;line-height:8px;color:#e8e8e8}
.foot-address b{color:var(--blue)}
.web{font-family:"Fira Sans",sans-serif;font-weight:600;color:var(--white);font-size:8.5px;letter-spacing:2.1px}

/* inside */
.about-col{left:18px;top:0;width:140px;height:480px;background:repeating-linear-gradient(45deg,#2a2a2c 0 1px,#252527 1px 3px)}
.about-title{left:30px;top:20px;font-family:"Bebas Neue",sans-serif;color:var(--blue);font-size:42px;line-height:42px}
.why-head{left:32px;top:84px;width:122px;font-family:"Fira Sans",sans-serif;font-weight:500;color:var(--white);font-size:9.6px;line-height:13px}
.why-copy{left:32px;top:122px;width:120px;font-size:5.3px;line-height:8.4px;color:#e3e3e3}
.why-list{left:34px;top:187px;width:120px;list-style:none}
.why-list li{position:relative;padding-left:14px;font-family:"Fira Sans",sans-serif;font-size:7.4px;line-height:9.3px;color:var(--white);margin-bottom:4px}
.why-list svg{position:absolute;left:0;top:1px;width:7px;height:7px}
.mid-panel{left:158px;top:0;width:179px;height:480px;background:var(--paper-mid)}
.right-panel{left:337px;top:0;width:337px;height:480px;background:var(--paper)}
.col-head{font-family:"Fira Sans",sans-serif;font-weight:600;color:var(--blue-deep);font-size:8.6px;line-height:10.6px}
.col-copy{font-size:5.1px;line-height:7.3px;color:var(--text);text-align:justify;margin-top:5px}
.big-title{left:353px;top:22px;font-family:"Oswald",sans-serif;font-weight:500;color:var(--grey);font-size:23px;line-height:30px;letter-spacing:.2px}
.title-bar{left:612px;top:34px;width:62px;height:8px;background:var(--grey)}
.brand-card{left:537px;top:92px;width:115px;height:240px}
.brand-text{left:537px;top:163px;width:115px;text-align:center;color:var(--white)}
.brand-text h3{font-family:"Fira Sans",sans-serif;font-weight:400;font-size:10.5px;line-height:12.5px}
.brand-text p{font-family:"Fira Sans",sans-serif;font-weight:400;font-size:7px;line-height:11px;margin-top:6px}
.strip{top:342px;height:91px}
.rule{left:0;top:451px;width:674px;height:8px;background:linear-gradient(90deg,var(--blue-deep) 0%,#5d87c9 25%,#e9eef8 50%,#e9eef8 52%,#5d87c9 78%,var(--blue-deep) 100%)}
.sq{width:13px;height:13px;background:#111;transform:rotate(45deg);top:449px}
</style>
</head>
<body>

<div class="label" style="left:298px;top:62px">BACK</div>
<div class="label" style="left:629px;top:62px">FRONT</div>

<!-- OUTSIDE SPREAD -->
<section class="spread outer">
  <div class="abs back-panel"></div>

  <svg class="abs" style="left:0;top:0" width="674" height="420" viewBox="0 0 674 420">
    <polygon points="214,0 674,0 674,128 504,240" fill="#a8a8a6" role="img" aria-label="Photo of a modern bathroom with twin basins, freestanding tub and a green living wall"/>
    <polygon points="184,0 218,0 440,222 424,238" fill="var(--blue)"/>
    <polygon points="674,123 674,160 584,245 566,228" fill="var(--blue-deep)"/>
    <polygon points="504,162 583,239 504,318 425,239" fill="var(--white)" stroke="var(--blue-deep)" stroke-width="4"/>
    <polygon points="448,368 593,368 580,413 428,413" fill="#9a8f84" role="img" aria-label="Photo of a bright kitchen with granite counters and steel appliances"/>
  </svg>

  <div class="abs" style="left:437px;top:209px;width:134px;text-align:center">
    <div class="brand-name" style="font-size:13px;line-height:14px">Hearth &amp; Tile<br>Crafters</div>
    <div style="font-family:'Fira Sans',sans-serif;font-weight:600;font-size:9.5px;color:var(--ink);margin-top:9px">515.482.7395</div>
  </div>

  <h2 class="abs back-title">Do you want to enhance the function of your kitchen and bathroom?</h2>
  <p class="abs back-copy">Do you want to enhance the function of your kitchen and bathroom? Perhaps you want to fix minor damage in your existing countertops? No matter what your needs are, Hearth &amp; Tile Crafters can help you. We are known for offering world-class countertop installation and repair services to residential and commercial properties in Ankeny, IA.</p>
  <h3 class="abs section-head" style="left:31px;top:154px;font-size:12px">Enhance the Look of Your Space</h3>
  <div class="photo" style="left:31px;top:174px;width:206px;height:66px;background:linear-gradient(90deg,#c9a27a,#efe9e1 55%,#8d6d4d)" role="img" aria-label="Photo of an open kitchen with a wood island and dining chairs"></div>
  <div class="photo" style="left:31px;top:247px;width:206px;height:66px;background:linear-gradient(90deg,#6b5a4a,#d8d6d2 55%,#a9a6a2)" role="img" aria-label="Photo of a kitchen and living room with a stone feature wall"></div>
  <div class="abs contact-head">Contact Our Remodelers Today!</div>
  <div class="abs contact-mail">hello@hearthtileia.net</div>

  <h2 class="abs tagline">We specialize in kitchen and bathroom renovations and counter installation</h2>

  <div class="abs footer-band"></div>
  <div class="abs footer-dark"></div>
  <div class="abs" style="left:26px;top:427px;display:flex;align-items:center;gap:5px">
    <span class="brand-mark" style="width:14px;height:14px"></span>
    <span class="brand-name" style="font-size:10.5px">Hearth &amp; Tile Crafters</span>
  </div>
  <div class="abs foot-phone">515.482.7395</div>
  <div class="abs foot-services">Residential Kitchen and Bath Remodeling &nbsp;|&nbsp; Countertop Installation and Repair<br>Kitchens, Bathrooms, and Countertops &nbsp;|&nbsp; Superior Remodeling Service</div>
  <div class="abs foot-address">782 NW Larkspur Lane Suite #217, Ankeny, Iowa 50894<br><b>Email:</b> htcraftersmidwest@pinemail.net</div>
  <div class="abs web" style="left:209px;top:457px">www.hearthtileia.net</div>
  <div class="abs web" style="left:337px;width:337px;top:456px;text-align:center">www.hearthtileia.net</div>
  <div class="fold"></div>
</section>

<!-- INSIDE SPREAD -->
<section class="spread inner">
  <div class="abs about-col" style="height:480px"></div>
  <div class="abs mid-panel"></div>
  <div class="abs right-panel"></div>

  <h1 class="abs about-title">ABOUT US</h1>
  <h2 class="abs why-head">WHY CHOOSE HEARTH &amp; TILE CRAFTERS?</h2>
  <p class="abs why-copy">The number one reason why you should partner with us is that we are the only company in the state licensed to do warranty work. With us, you can be confident that your projects are in safe, dependable hands. Here are more reasons to choose us:</p>
  <ul class="abs why-list">
    <li><svg viewBox="0 0 10 10"><circle cx="5" cy="5" r="5" fill="var(--blue)"/><path d="M2.6 5.2l1.7 1.7 3.2-3.4" stroke="#fff" stroke-width="1.3" fill="none"/></svg>Fully Insured and Licensed Business</li>
    <li><svg viewBox="0 0 10 10"><circle cx="5" cy="5" r="5" fill="var(--blue)"/><path d="M2.6 5.2l1.7 1.7 3.2-3.4" stroke="#fff" stroke-width="1.3" fill="none"/></svg>Listed on HomePro Finder</li>
    <li><svg viewBox="0 0 10 10"><circle cx="5" cy="5" r="5" fill="var(--blue)"/><path d="M2.6 5.2l1.7 1.7 3.2-3.4" stroke="#fff" stroke-width="1.3" fill="none"/></svg>Serves Residential and Commercial Clients</li>
    <li><svg viewBox="0 0 10 10"><circle cx="5" cy="5" r="5" fill="var(--blue)"/><path d="M2.6 5.2l1.7 1.7 3.2-3.4" stroke="#fff" stroke-width="1.3" fill="none"/></svg>Various Payment Options Accepted</li>
    <li><svg viewBox="0 0 10 10"><circle cx="5" cy="5" r="5" fill="var(--blue)"/><path d="M2.6 5.2l1.7 1.7 3.2-3.4" stroke="#fff" stroke-width="1.3" fill="none"/></svg>Countertop Installation and Repair</li>
  </ul>

  <div class="abs" style="left:172px;top:30px;display:flex;align-items:center;gap:6px">
    <span class="brand-mark" style="width:18px;height:18px"></span>
    <span class="brand-name" style="font-size:11px">Hearth &amp; Tile Crafters</span>
  </div>

  <div class="abs" style="left:172px;top:88px;width:154px">
    <h3 class="col-head">Residential Kitchen and Bath Remodeling</h3>
    <p class="col-copy">Having a fulfilling mealtime with your family or a calming bath after a long day at work can easily drive your stress away. But does the current look of your kitchen and bathroom take away these simple joys from you? This is the time when having Hearth &amp; Tile Crafters in Ankeny, IA by your side comes to your advantage. We can create your own personal sanctuary at home by offering our residential kitchen and bath remodeling services.</p>
    <h3 class="col-head" style="margin-top:9px">Make Your Office Kitchen More Inviting</h3>
    <p class="col-copy">Do you find preparing meals a relaxing and gratifying task? Hire our remodelers today and allow us to do kitchen remodeling and redesigning not only for your home but also for your workplace. From building more room in your kitchen to installing suitable countertops in your office pantry, we have you covered. We carry different countertop materials for your added convenience.</p>
    <h3 class="col-head" style="margin-top:9px">Your Source for Quality Countertops</h3>
    <p class="col-copy">If you are in the market for the best countertop material for your space, look no further than Hearth &amp; Tile Crafters. Our services are not limited to countertop installation and maintenance. We also have a wide variety of countertop materials available for sale. Reach us today for more details about our product and service offerings.</p>
  </div>

  <h2 class="abs big-title">Hearth &amp; Tile Crafters</h2>
  <div class="abs title-bar"></div>

  <div class="abs" style="left:353px;top:88px;width:170px">
    <h3 class="col-head">Your Source for Quality Countertops</h3>
    <p class="col-copy">If you are in the market for the best countertop material for your space, look no further than Hearth &amp; Tile Crafters. Our services are not limited to countertop installation and maintenance. We also have a wide variety of countertop materials available for sale. Reach us today for more details about our product and service offerings.</p>
    <h3 class="col-head" style="margin-top:13px">More Than Just Countertop Services</h3>
    <p class="col-copy">Nothing beats Hearth &amp; Tile Crafters when it comes to providing countertop services. Our business is not only about installing or repairing countertops for a residential or commercial property. We can also handle kitchen and bathroom renovation projects for your home or business establishment. Led by Reid Calloway, our remodelers are dedicated to bringing your dream space to life. Our countertop services, including our bath and kitchen renovation solutions, are available within a 50-mile radius of our office in Ankeny, IA. Contact us for more details.</p>
    <h3 class="col-head" style="margin-top:13px">Contact Our Remodelers Today!</h3>
    <p class="col-copy">Tick off your remodeling project checklist. When it comes to countertop installation and repair, trust none other than Hearth &amp; Tile Crafters. Our team can do more than just selling and servicing countertops. You can also rely on us for your commercial or residential kitchen and bath remodeling needs. Give us a call or send us an email to speak with one of our remodelers.</p>
  </div>

  <svg class="abs brand-card" viewBox="0 0 115 240">
    <path d="M4 0H111a4 4 0 0 1 4 4V206L57.5 238 0 206V4a4 4 0 0 1 4-4z" fill="var(--grey)"/>
    <rect x="3" y="3" width="109" height="64" fill="#7d6f63" role="img" aria-label="Photo of countertop stone and laminate samples fanned out"/>
    <path d="M3 144H112V204L57.5 234 3 204z" fill="#b08a6c" role="img" aria-label="Photo of a kitchen with warm wood cabinetry"/>
  </svg>
  <div class="abs brand-text">
    <h3>Brands We Carry Include</h3>
    <p>Corvane, Tavelle<br>Granvale, Veloria,<br>Quarnix, Marbleton</p>
  </div>

  <div class="abs strip" style="left:0;width:187px;background:linear-gradient(90deg,#8a8a88,#b8a489 70%,#d9d8d4)" role="img" aria-label="Photo of a grey tiled bathroom with a wood-panelled tub"></div>
  <div class="abs strip" style="left:187px;width:165px;background:linear-gradient(90deg,#e8e6e2,#f4f3f0 50%,#d6d1c8)" role="img" aria-label="Photo of a bright white bathroom with a freestanding tub"></div>
  <div class="abs strip" style="left:352px;width:202px;background:linear-gradient(90deg,#4b3b2e,#c7b8a4 55%,#7e6a55)" role="img" aria-label="Photo of a bathroom with dark vanity and soaking tub"></div>
  <div class="abs strip" style="left:554px;width:120px;background:linear-gradient(90deg,#e9e5de,#b3835a 70%,#d8d2c8)" role="img" aria-label="Photo of a kitchen island with bar stools"></div>

  <div class="abs about-col" style="top:433px;height:47px"></div>
  <div class="abs rule"></div>
  <div class="abs sq" style="left:19px"></div>
  <div class="abs sq" style="left:642px"></div>
  <div class="fold"></div>
</section>

<div class="label" style="left:304px;top:1115px">Front inside</div>
<div class="label" style="left:634px;top:1115px">Back inside</div>

</body>
</html>
```